Website Design for Gold Buying Company in Australia

We are looking for a Website layout for a company who buy gold pieces from trade and the public.

They would like to communicate that its easy, safe, a great way to make more money, and they pay the best prices in australia for Gold jewelery

Target Market(s)

Adults based in Australia aged 25-60 who are looking to make some extra money

Industry/Entity Type

It Company

Number of Pages Required

2 pages

Requirements
Must have
• Must have a homepage and a page to use for content.

• Will have a feed for the latest Gold, silver and platinum prices they are buying and selling at.

• Needs to have a from on the homepage where people can submit their details to be sent a ''Nugget Box'' which allows them to send gold pieces to eb valued and bought by the company.

Nice to have
• Would be nice to have a steped out graphic of how the ''Nugget Box by mail'' process works [Request a Kit, Send in your Gold, We Value and grade it, We pay you cash, cheque of Direct Deposit]

• Imagery will be gold related

• Colour schemes are not a major Issue-but using some gold or silver would be a good idea
Should not have
• No cheesy gold graphics please :)

```html
<!DOCTYPE html>
<html lang="en">
<head>
<meta charset="utf-8">
<title>Aurevale – Gold Buyers Australia</title>
<link href="https://fonts.googleapis.com/css2?family=Questrial&family=Montserrat:wght@700;800&family=Arimo:wght@400;700&display=swap" rel="stylesheet">
<style>
:root{
  --gold-light:#e2c59a;
  --brown:#a3581c;
  --brown-text:#b0621f;
  --slate:#8d9aa3;
  --ink:#3b3b3b;
  --body:#555;
  --nav-top:#3e4245;
  --nav-bottom:#16191b;
  --cream:#faf5ee;
  --footer:#e6e6e6;
  --field-line:#c9c9c9;
  --link-blue:#3b7fd0;
}
*{margin:0;padding:0;box-sizing:border-box}
html,body{width:1200px;height:658px;overflow:hidden;background:#fff}
body{position:relative;font-family:"Arimo",Arial,sans-serif}
.page{position:absolute;top:0;width:600px;height:658px;overflow:hidden;background:#fff;border-top:2px solid #9a9a9a}
.page--home{left:0}
.page--content{left:601px;border-left:1px solid #fff}
.abs{position:absolute}

.brand{left:43px;top:17px;font-family:"Questrial",sans-serif;font-size:38px;line-height:46px;color:var(--gold-light);letter-spacing:-.8px;white-space:nowrap}
.util-icons{left:470px;top:31px;display:flex;gap:18px}
.util-icons svg{width:12px;height:12px}
.trade-link{left:462px;top:60px;font-family:"Questrial",sans-serif;font-size:11.5px;color:var(--brown-text)}

.nav-band{left:0;top:78px;width:600px;height:64px;background:linear-gradient(var(--nav-top),var(--nav-bottom))}
.nav{left:0;top:78px;width:600px;height:32px;list-style:none;font-family:"Questrial",sans-serif;font-size:11.5px;color:#fff}
.nav li{position:absolute;top:0;height:32px;line-height:32px;text-align:center;transform:translateX(-50%);white-space:nowrap}
.nav .sep{width:1px;height:30px;top:1px;background:#2a2d2f;transform:none}
.nav-tab{top:77px;width:78px;height:31px;background:#fff;border-radius:6px}
.nav li.is-active{color:var(--brown-text)}

.hero{left:22px;top:115px;width:561px;height:183px;border-radius:9px 9px 0 0;overflow:hidden;
  background:radial-gradient(ellipse at 25% 55%,#d6a545 0%,#a9742a 35%,#7d5322 60%,#b89570 85%,#c9ad8d 100%)}
.hero-copy{right:26px;top:52px;width:190px;height:110px;font-family:"Questrial",sans-serif;color:#fff}
.hero-best{right:62px;top:0;font-size:44px;line-height:44px;letter-spacing:-1px}
.hero-prices{left:0;top:46px;font-family:"Montserrat",sans-serif;font-weight:800;font-size:16px;line-height:18px}
.hero-aus{right:0;top:58px;font-size:28px;line-height:30px;letter-spacing:-.5px}

.content-bg{left:0;top:298px;width:600px;height:302px;background:var(--cream)}
.kit-panel{left:22px;top:298px;width:561px;height:123px;border-radius:0 0 10px 10px;background:linear-gradient(#fff 60%,#eef0f2);box-shadow:0 2px 3px rgba(0,0,0,.18)}
.kit-request{left:47px;top:310px;font-family:"Questrial",sans-serif;font-size:15px;color:var(--slate)}
.kit-name{left:47px;top:325px;font-family:"Montserrat",sans-serif;font-weight:800;font-size:25px;color:var(--brown);letter-spacing:-.5px}
.kit-today{left:93px;top:355px;font-family:"Questrial",sans-serif;font-size:15px;color:var(--slate)}
.kit-steps{left:48px;top:381px;width:180px;font-size:7.3px;line-height:10.5px;letter-spacing:.6px;color:#333}
.kit-required{left:189px;top:402px;font-size:8px;color:var(--brown-text);text-decoration:underline}
.field{position:absolute;height:17px;border:1px solid var(--field-line);background:#fff;font-size:8px;line-height:15px;padding-left:7px;color:#8a8a8a;box-shadow:inset 1px 1px 0 #eee}
.kit-button{left:420px;top:336px;width:150px;height:44px;border-radius:10px;border:2px solid #c49a3a;
  background:linear-gradient(#f3dfa3,#c9962f 45%,#a4731c 55%,#e6c66e);font-family:"Montserrat",sans-serif;font-weight:800;font-size:17px;color:#fff;text-align:center;line-height:40px;text-shadow:0 1px 1px rgba(80,50,0,.6)}

.section-title{font-family:"Questrial",sans-serif;font-size:17px;color:var(--slate);line-height:16px;white-space:nowrap}
.section-title b{font-family:"Montserrat",sans-serif;font-weight:800;color:var(--brown);font-size:16px}
.section-sub{font-family:"Questrial",sans-serif;font-size:8.5px;line-height:9px;color:var(--ink);white-space:nowrap}
.copy{width:248px;font-size:8px;line-height:10.3px;color:var(--body)}
.copy strong{color:var(--brown-text);font-size:8.5px}
.copy a{color:var(--brown-text)}
.news{left:317px;top:471px;width:245px;list-style:none;font-size:8.4px;color:var(--body)}
.news li{height:18px;line-height:16px;border-bottom:1px solid #e2ded7;white-space:nowrap;overflow:hidden}
.news .arrow{color:var(--link-blue);margin:0 4px 0 3px;font-size:7px}
.news .date{color:var(--brown-text)}
.more-link{font-size:8.5px;color:var(--brown-text)}
.more-link span{text-decoration:underline}

.footer{left:0;top:600px;width:600px;height:58px;background:var(--footer);border-top:1px solid #d4d4d4}
.footer-note{left:38px;top:625px;font-size:7.5px;letter-spacing:.6px;color:#666}
.footer-links{left:440px;top:625px;font-size:7.5px;letter-spacing:.6px;color:#666}
.footer-links span{text-decoration:underline}
</style>
</head>
<body>

<!-- Home page -->
<div class="page page--home">
  <div class="abs brand">AUREVALE.COM.AU</div>
  <div class="abs util-icons">
    <svg viewBox="0 0 12 12"><path d="M1 6 6 1.5 11 6M2.5 5v5.5h7V5" fill="none" stroke="#333" stroke-width="1.3"/></svg>
    <svg viewBox="0 0 12 12" fill="none" stroke="#777" stroke-width="1"><rect x="4" y="1" width="4" height="3"/><path d="M6 4v2M2 6h8M2 6v2M6 6v2M10 6v2"/><rect x="1" y="8" width="2" height="2"/><rect x="5" y="8" width="2" height="2"/><rect x="9" y="8" width="2" height="2"/></svg>
    <svg viewBox="0 0 12 12" fill="none" stroke="#777" stroke-width="1"><rect x="1" y="3" width="10" height="7"/><path d="M1 3l5 4 5-4"/></svg>
  </div>
  <div class="abs trade-link">TRADE ENQUIRIES</div>

  <div class="abs nav-band"></div>
  <div class="abs nav-tab" style="left:36px"></div>
  <ul class="abs nav">
    <li class="is-active" style="left:74px">ABOUT US</li>
    <li style="left:166px">BUY &amp; SELL</li>
    <li class="sep" style="left:203px"></li>
    <li style="left:254px">HOW IT WORKS</li>
    <li class="sep" style="left:304px"></li>
    <li style="left:353px">QUESTIONS</li>
    <li class="sep" style="left:396px"></li>
    <li style="left:438px">BULLION</li>
    <li class="sep" style="left:476px"></li>
    <li style="left:521px">CONTACTS</li>
  </ul>

  <div class="abs hero" role="img" aria-label="Close-up photograph of a pile of gold jewellery, chains and coins">
    <div class="abs hero-copy">
      <div class="abs hero-best">BEST</div>
      <div class="abs hero-prices">PRICES IN</div>
      <div class="abs hero-aus">AUSTRALIA</div>
    </div>
  </div>

  <div class="abs content-bg"></div>
  <div class="abs kit-panel"></div>
  <div class="abs kit-request">REQUEST YOUR</div>
  <div class="abs kit-name">NUGGET BOX</div>
  <div class="abs kit-today">TODAY</div>
  <p class="abs kit-steps">Send in your Gold, We Value and grade it, We pay you cash, cheque of Direct Deposit</p>
  <div class="abs kit-required">*Required</div>
  <div class="field" style="left:233px;top:304px;width:157px">First Name*</div>
  <div class="field" style="left:233px;top:322px;width:157px">Last Name*</div>
  <div class="field" style="left:233px;top:341px;width:172px">Address*</div>
  <div class="field" style="left:233px;top:360px;width:126px">City*</div>
  <div class="field" style="left:361px;top:360px;width:26px">Stat</div>
  <div class="field" style="left:233px;top:378px;width:50px">Zip*</div>
  <div class="field" style="left:286px;top:378px;width:101px">Phone</div>
  <div class="field" style="left:233px;top:397px;width:172px">Email*</div>
  <div class="abs kit-button">GET YOUR KIT!</div>

  <div class="abs section-title" style="left:41px;top:434px"><b>WHO</b> WE ARE</div>
  <div class="abs section-sub" style="left:41px;top:451px">COMPANY PROFILE OVERVIEW</div>
  <div class="abs section-title" style="left:317px;top:434px"><b>WHAT</b> WE DO</div>
  <div class="abs section-sub" style="left:317px;top:451px">FEATURED SERVICES</div>

  <div class="abs copy" style="left:41px;top:472px">
    <strong>Aliquam vitae lorem da.</strong><br>
    Integer pede nisi, adipng eget, gravida sagittis, placerat vel. Sed a us id <a>nisi feugiat</a> convallis. Vivamus telluse urna, tincidunt vel, commodo sit amet, viverra vitae, enim. Donec vitae odio.
  </div>
  <div class="abs copy" style="left:41px;top:527px">
    <strong>Vivamus telluse urna</strong>, tincidunt vel, <a>commodo sit amet</a>, viverra ec vitae odio. Vivamus ut turpis. Cras arcu. tortor. Sed lesuada isse porttitor, mi id tincidunt tristique, nulla nisi feugiat libero.
  </div>

  <ul class="abs news">
    <li><span class="arrow">⇢</span><span class="date">2007-06-10</span> / Lorem ipsum dolor sit amet consectetuer adipis</li>
    <li><span class="arrow">⇢</span><span class="date">2007-06-12</span> / Consectetuer adipiscing elit hasellus sapien</li>
    <li><span class="arrow">⇢</span><span class="date">2007-06-10</span> / Lorem ipsum dolor sit amet consectetuer adipi</li>
    <li><span class="arrow">⇢</span><span class="date">2007-06-12</span> / Phasellus sapien tortor, fringilla vel, pretium</li>
    <li><span class="arrow">⇢</span><span class="date">2007-06-12</span> / Nulla mi urna, faucibus eget, faucibus idodo</li>
  </ul>

  <div class="abs more-link" style="left:223px;top:572px"><span>more about us</span> &gt;&gt;</div>
  <div class="abs more-link" style="left:505px;top:572px"><span>all services</span> &gt;&gt;</div>

  <div class="abs footer"></div>
  <div class="abs footer-note">AUREVALE 2009. All rights reserved</div>
  <div class="abs footer-links"><span>Privacy Policy</span> &nbsp;and&nbsp; <span>Terms of Use</span></div>
</div>

<!-- Content page -->
<div class="page page--content">
  <div class="abs brand">AUREVALE.COM.AU</div>
  <div class="abs util-icons">
    <svg viewBox="0 0 12 12"><path d="M1 6 6 1.5 11 6M2.5 5v5.5h7V5" fill="none" stroke="#333" stroke-width="1.3"/></svg>
    <svg viewBox="0 0 12 12" fill="none" stroke="#777" stroke-width="1"><rect x="4" y="1" width="4" height="3"/><path d="M6 4v2M2 6h8M2 6v2M6 6v2M10 6v2"/><rect x="1" y="8" width="2" height="2"/><rect x="5" y="8" width="2" height="2"/><rect x="9" y="8" width="2" height="2"/></svg>
    <svg viewBox="0 0 12 12" fill="none" stroke="#777" stroke-width="1"><rect x="1" y="3" width="10" height="7"/><path d="M1 3l5 4 5-4"/></svg>
  </div>
  <div class="abs trade-link">TRADE ENQUIRIES</div>

  <div class="abs nav-band"></div>
  <div class="abs nav-tab" style="left:122px"></div>
  <ul class="abs nav">
    <li style="left:74px">ABOUT US</li>
    <li class="is-active" style="left:161px">BUY &amp; SELL</li>
    <li style="left:254px">HOW IT WORKS</li>
    <li class="sep" style="left:304px"></li>
    <li style="left:353px">QUESTIONS</li>
    <li class="sep" style="left:396px"></li>
    <li style="left:438px">BULLION</li>
    <li class="sep" style="left:476px"></li>
    <li style="left:521px">CONTACTS</li>
  </ul>

  <div class="abs hero" role="img" aria-label="Close-up photograph of a pile of gold jewellery, chains and coins">
    <div class="abs hero-copy">
      <div class="abs hero-best">BEST</div>
      <div class="abs hero-prices">PRICES IN</div>
      <div class="abs hero-aus">AUSTRALIA</div>
    </div>
  </div>

  <div class="abs content-bg"></div>
  <div class="abs kit-panel"></div>
  <div class="abs kit-request">REQUEST YOUR</div>
  <div class="abs kit-name">NUGGET BOX</div>
  <div class="abs kit-today">TODAY</div>
  <p class="abs kit-steps">Send in your Gold, We Value and grade it, We pay you cash, cheque of Direct Deposit</p>
  <div class="abs kit-required">*Required</div>
  <div class="field" style="left:233px;top:304px;width:157px">First Name*</div>
  <div class="field" style="left:233px;top:322px;width:157px">Last Name*</div>
  <div class="field" style="left:233px;top:341px;width:172px">Address*</div>
  <div class="field" style="left:233px;top:360px;width:126px">City*</div>
  <div class="field" style="left:361px;top:360px;width:26px">Stat</div>
  <div class="field" style="left:233px;top:378px;width:50px">Zip*</div>
  <div class="field" style="left:286px;top:378px;width:101px">Phone</div>
  <div class="field" style="left:233px;top:397px;width:172px">Email*</div>
  <div class="abs kit-button">GET YOUR KIT!</div>

  <div class="abs section-title" style="left:40px;top:436px"><b>WHAT</b> WE BUY</div>

  <div class="abs copy" style="left:39px;top:472px">
    <strong>Aliquam vitae lorem da.</strong><br>
    Integer pede nisi, adipng eget, gravida sagittis, placerat vel. Sed a us id <a>nisi feugiat</a> convallis. Vivamus telluse urna, tincidunt vel, commodo sit amet, viverra vitae, enim. Donec vitae odio.
  </div>
  <div class="abs copy" style="left:39px;top:527px">
    <strong>Vivamus telluse urna</strong>, tincidunt vel, <a>commodo sit amet</a>, viverra ec vitae odio. Vivamus ut turpis. Cras arcu. tortor. Sed lesuada isse porttitor, mi id tincidunt tristique, nulla nisi feugiat libero.
  </div>
  <div class="abs copy" style="left:327px;top:472px">
    <strong>Aliquam vitae lorem da.</strong><br>
    Integer pede nisi, adipng eget, gravida sagittis, placerat vel. Sed a us id <a>nisi feugiat</a> convallis. Vivamus telluse urna, tincidunt vel, commodo sit amet, viverra vitae, enim. Donec vitae odio.
  </div>
  <div class="abs copy" style="left:327px;top:527px">
    <strong>Vivamus telluse urna</strong>, tincidunt vel, <a>commodo sit amet</a>, viverra ec vitae odio. Vivamus ut turpis. Cras arcu. tortor. Sed lesuada isse porttitor, mi id tincidunt tristique, nulla nisi feugiat libero.
  </div>

  <div class="abs footer"></div>
  <div class="abs footer-note">AUREVALE 2009. All rights reserved</div>
  <div class="abs footer-links"><span>Privacy Policy</span> &nbsp;and&nbsp; <span>Terms of Use</span></div>
</div>

</body>
</html>
```